Classy, Elegant, Simple Business Card Design

Looking to have a classy, simple, and elegant design. Want a top notch designed business card. I really like the look of the new brivo credit card. I also like the design I attached. I am trying to reach 21-29 year old females for booking us for there wedding or event. We offer Disc Jockey Service, Photo Booth Rentals, and Uplighting .

Target Market(s)

21-28 year old females

Contact Information for Business Card

Has to have logo, website, email, and phone number

Font styles to use
Other font styles liked:
• open to font choice, modern, clean
Designer to choose
33a6d7
0791cd
0555a3
ffffff

Requirements
Must have
• Has to have logo, website, email, and phone number
Nice to have
• I really like the design of the new brivo credit card. I also included my logo and some designs I like
Should not have
• clutter or too much info

```html
<!DOCTYPE html>
<html lang="en">
<head>
<meta charset="utf-8">
<title>Tidewell Event Group — Business Card</title>
<link rel="stylesheet" href="https://fonts.googleapis.com/css2?family=Poppins:wght@400;500&display=swap">
<style>
  :root {
    --sky: #33a6d7;
    --azure: #0791cd;
    --navy: #0555a3;
    --white: #ffffff;
    --ink: #3d3d3d;
    --muted: #9a9a9a;
    --tab: #b4b4b4;
    --backdrop: #dcdcdc;
  }
  * { margin: 0; padding: 0; box-sizing: border-box; }
  html, body { width: 1200px; height: 1200px; overflow: hidden; }
  body {
    background: var(--backdrop);
    font-family: "Poppins", sans-serif;
    position: relative;
  }
  .card {
    position: absolute;
    left: 262px;
    width: 686px;
    height: 392px;
    overflow: hidden;
  }
  .card--front { top: 165px; background: var(--white); }
  .card--back {
    top: 653px;
    background: radial-gradient(ellipse at 50% 55%, #0aa6e3 0%, #1896d6 45%, #1a7fc6 100%);
  }

  /* front */
  .accent-bar {
    position: absolute; left: 0; top: 41px; width: 9px; height: 123px;
    background: linear-gradient(180deg, var(--sky), var(--navy));
  }
  .edge-tab {
    position: absolute; right: 0; top: 207px; width: 10px; height: 124px;
    background: var(--tab);
  }
  .identity { position: absolute; left: 31px; top: 42px; }
  .identity__name {
    font-size: 24px; font-weight: 500; color: var(--azure); line-height: 1.15;
    letter-spacing: 0.3px;
  }
  .identity__role { font-size: 15.5px; color: var(--muted); line-height: 1.3; }
  .contacts { position: absolute; left: 31px; top: 111px; list-style: none; }
  .contacts li {
    display: flex; align-items: center; gap: 9px;
    font-size: 15.5px; color: var(--ink); line-height: 19.5px;
  }
  .contacts svg { width: 15px; height: 15px; flex: none; }

  .brand {
    position: absolute; left: 400px; top: 240px; width: 250px;
    display: flex; align-items: center; justify-content: center; gap: 10px;
  }
  .brand__dot { width: 14px; height: 14px; border-radius: 50%; background: var(--azure); }
  .brand__name {
    font-size: 30px; font-weight: 500; color: var(--navy); letter-spacing: 1px;
  }

  /* back */
  .brand--back {
    position: absolute; left: 0; right: 0; top: 130px;
    text-align: center;
    font-size: 64px; font-weight: 500; color: var(--white); letter-spacing: 2px;
  }
  .services {
    position: absolute; left: 0; right: 0; top: 332px;
    text-align: center; font-size: 16.5px; color: var(--white);
  }
</style>
</head>
<body>
  <section class="card card--front" aria-label="Card front">
    <div class="accent-bar"></div>
    <div class="edge-tab"></div>

    <div class="identity">
      <p class="identity__name">Daniel Hart</p>
      <p class="identity__role">President</p>
    </div>

    <ul class="contacts">
      <li>
        <svg viewBox="0 0 16 16" aria-hidden="true"><path fill="#0791cd" d="M2 5c0-2 2.5-3 6-3s6 1 6 3v1.5h-3V5H5v1.5H2zM4 7h8l2 7H2zm4 1.8a2 2 0 100 4 2 2 0 000-4z"/></svg>
        555-014-2278
      </li>
      <li>
        <svg viewBox="0 0 16 16" aria-hidden="true"><rect x="1" y="4" width="14" height="9" fill="#0791cd"/><path d="M1 4l7 5 7-5" fill="none" stroke="#fff" stroke-width="1.2"/></svg>
        info@tidewellevents.com
      </li>
      <li>
        <svg viewBox="0 0 16 16" aria-hidden="true"><circle cx="8" cy="8" r="7" fill="#0791cd"/><path d="M5 4c2 1 1 3 3 3s1 3 3 3M9 12c-1-1 0-2-1-3" fill="none" stroke="#fff" stroke-width="1.2"/></svg>
        www.tidewellevents.com
      </li>
    </ul>

    <div class="brand">
      <span class="brand__dot"></span>
      <span class="brand__name">TIDEWELL</span>
    </div>
  </section>

  <section class="card card--back" aria-label="Card back">
    <p class="brand--back">Tidewell</p>
    <p class="services">Disc Jockey Service • Photo Booth Rentals • Uplighting</p>
  </section>
</body>
</html>
```